Website design needed for Renewable utilities company based in New Zealand.

Website design needed for Lanternvale Holdings based in New Zealand.

Please see attached logo.

We sell solar panels, vertical axis wind turbines, atmospheric water generators and other related equipment for those who don't have access or don't want to depend on the government, city councils for their utilities (power and water).

We like metallic texture, dark grey and purple, red or blue colours. The design should go well with the attached logo.

Target Market(s)

The Eco conscious

Industry/Entity Type

Government

Logo Text

Lanternvale Summit

Requirements
Must have
• Must Have:
- Metallic finish is a must.
- Design should fit around the attached logo well.
Nice to have
• Sharpe design prefred rather than rounded edges

```html
<!DOCTYPE html>
<html lang="en">
<head>
<meta charset="utf-8">
<title>Lanternvale Summit</title>
<link rel="stylesheet" href="https://fonts.googleapis.com/css2?family=Arimo:wght@400;700&display=swap">
<style>
:root{
  --steel-dark:#5e5e5e;
  --steel-mid:#b9b9b9;
  --steel-light:#e6e6e6;
  --brand-blue:#1b7fbd;
  --nav-top:#4a95cc;
  --nav-bottom:#1d5f93;
  --navy:#1d2c44;
  --text-grey:#5a5a5a;
  --rule:#a9a9a9;
  --white:#ffffff;
  --social-grey:#8d8d8d;
  --tw:#1da1e2;
  --li:#1679ad;
  --fb:#3b5a97;
  --yt:#e0141d;
}
*{margin:0;padding:0;box-sizing:border-box}
html,body{width:1141px;height:1200px;overflow:hidden}
body{position:relative;font-family:"Arimo",Arial,sans-serif;background:var(--steel-mid)}
.abs{position:absolute}

.top-strip{left:0;top:0;width:1141px;height:20px;background:linear-gradient(#7a7a7a,#4f4f4f)}
.header{left:0;top:20px;width:1141px;height:200px;background:linear-gradient(#e4e4e4,#d2d2d2 60%,#a8a8a8)}
.brand-mark{left:214px;top:26px;width:64px;height:64px;border-radius:50%;background:radial-gradient(circle at 40% 35%,#2f8fd6,#0a3f8a)}
.brand-name{left:146px;top:100px;width:202px;text-align:center;font-size:21px;color:var(--navy);white-space:nowrap}
.social{width:35px;height:35px;border-radius:50%}
.social.header-icon{background:var(--social-grey);top:42px;box-shadow:inset 0 1px 2px rgba(0,0,0,.3)}
.search{left:836px;top:95px;width:168px;height:35px;background:var(--white);border:1px solid #b9d2ea;font-size:13px;color:#9a9a9a;padding:10px 9px;letter-spacing:.5px}
.search-btn{left:1008px;top:95px;width:35px;height:35px;background:linear-gradient(#3f8fcf,#1b5f98)}
.header-rule{left:62px;top:150px;width:1015px;height:1px;background:var(--rule)}

.hero{left:0;top:220px;width:1141px;height:373px}
.hero-photo{left:0;top:0;width:1141px;height:373px;background:linear-gradient(110deg,#1a3f86 0%,#2e5fb0 40%,#3f86d6 70%,#6fb3ea 100%)}
.hero-panel{left:719px;top:0;width:306px;height:373px;background:rgba(22,38,66,.72);color:var(--white);padding:0 22px}
.hero-title{margin-top:50px;font-size:16px;font-weight:400;letter-spacing:1.2px}
.hero-copy{margin-top:18px;font-size:13.5px;line-height:19px;letter-spacing:.4px;text-align:justify;hyphens:auto;-webkit-hyphens:auto}
.hero-copy+.hero-copy{margin-top:19px}
.hero-call{left:22px;top:298px;font-size:18px;letter-spacing:.8px;display:flex;align-items:center;gap:12px}
.dots{left:25px;top:339px;display:flex;gap:8px}
.dots span{width:12px;height:12px;border-radius:50%;background:rgba(255,255,255,.65)}
.arrow{width:38px;height:38px;border-radius:50%;background:rgba(20,60,100,.75);top:177px}

.nav{left:155px;top:187px;width:842px;height:45px;background:linear-gradient(var(--nav-top),var(--nav-bottom));box-shadow:0 2px 4px rgba(0,0,0,.35);color:var(--white);font-size:15px;letter-spacing:.8px}
.nav-item{top:13px;transform:translateX(-50%);white-space:nowrap}
.nav-home{left:11px;top:11px;width:63px;height:24px;background:rgba(255,255,255,.22);border-radius:2px}

.features{left:0;top:593px;width:1141px;height:294px;background:linear-gradient(#c2c2c2,#d6d6d6)}
.features-rule{left:115px;top:20px;width:962px;height:1px;background:var(--rule)}
.feature-frame{top:37px;width:266px;height:184px;background:#a9a9a9;padding:7px}
.feature-photo{width:100%;height:100%}
.feature-title{top:229px;width:266px;text-align:center;font-size:22px;letter-spacing:1px;color:var(--navy)}
.feature-title b{font-weight:400;color:var(--brand-blue)}

.about{left:0;top:887px;width:1141px;height:257px;background:linear-gradient(#a9a9a9,#c9c9c9 40%,#d3d3d3);border-top:1px solid #9a9a9a}
.about-title{top:29px;width:1141px;text-align:center;font-size:22px;font-weight:400;letter-spacing:1px;color:var(--navy)}
.about-title b{font-weight:400;color:var(--brand-blue)}
.about-rule{left:115px;top:64px;width:962px;height:1px;background:var(--rule)}
.about-copy{left:130px;top:78px;width:932px;text-align:center;font-size:14px;line-height:27px;letter-spacing:1.1px;color:var(--text-grey)}
.social.footer-icon{top:181px;width:36px;height:36px}

.footer{left:0;top:1144px;width:1141px;height:56px;background:repeating-linear-gradient(135deg,#5a5a5a 0 2px,#626262 2px 4px);color:var(--white);font-size:11px;letter-spacing:1px}
.footer-links{left:125px;top:22px}
.footer-links span{margin:0 9px}
.copyright{right:77px;top:22px}
</style>
</head>
<body>
<div class="abs top-strip"></div>

<header class="abs header">
  <div class="abs brand-mark"></div>
  <div class="abs brand-name">Lanternvale Summit</div>
  <a class="abs social header-icon" style="left:846px" aria-label="Social network link"></a>
  <a class="abs social header-icon" style="left:895px" aria-label="Social network link"></a>
  <a class="abs social header-icon" style="left:942px" aria-label="Social network link"></a>
  <a class="abs social header-icon" style="left:990px" aria-label="Social network link"></a>
  <div class="abs search">Keyword Search</div>
  <div class="abs search-btn">
    <svg width="35" height="35" viewBox="0 0 35 35"><circle cx="14" cy="14" r="6" fill="none" stroke="#fff" stroke-width="3"/><line x1="18.5" y1="18.5" x2="27" y2="26" stroke="#fff" stroke-width="4" stroke-linecap="round"/></svg>
  </div>
  <div class="abs header-rule"></div>
</header>

<section class="abs hero">
  <div class="abs hero-photo" role="img" aria-label="Close view of a large solar panel array under a blue sky"></div>
  <div class="abs arrow" style="left:23px"><svg width="38" height="38"><polyline points="22,11 15,19 22,27" fill="none" stroke="#0e2e52" stroke-width="3"/></svg></div>
  <div class="abs arrow" style="left:1079px"><svg width="38" height="38"><polyline points="16,11 23,19 16,27" fill="none" stroke="#cfe6f7" stroke-width="3"/></svg></div>
  <div class="abs hero-panel">
    <h2 class="hero-title">HEADING GOES HERE</h2>
    <p class="hero-copy">Lorem ipsum dolor sit amet, consectetur adipiscing elit. Nam lobortis dolor cursus nisl suscipit convallis.</p>
    <p class="hero-copy">vel consequat metus euismod at. Phasellus porttitor ipsum sapien, vitae lacinia sem ultricies ut.</p>
    <div class="abs hero-call">
      <svg width="22" height="18" viewBox="0 0 22 18"><path d="M1 6 Q11 -2 21 6 L18 9 L15 6 L7 6 L4 9 Z" fill="#fff"/><rect x="4" y="9" width="14" height="8" rx="1" fill="#fff"/><circle cx="11" cy="13" r="2.3" fill="#1e3354"/></svg>
      <span>Call us 1-800-555-0142</span>
    </div>
    <div class="abs dots"><span></span><span></span><span></span><span></span></div>
  </div>
</section>

<nav class="abs nav">
  <div class="abs nav-home"></div>
  <span class="abs nav-item" style="left:43px">Home</span>
  <span class="abs nav-item" style="left:186px">About us</span>
  <span class="abs nav-item" style="left:388px">Our Products</span>
  <span class="abs nav-item" style="left:584px">Promos</span>
  <span class="abs nav-item" style="left:770px">Contact us</span>
</nav>

<section class="abs features">
  <div class="abs features-rule"></div>
  <div class="abs feature-frame" style="left:133px"><div class="feature-photo" role="img" aria-label="Technician installing a rooftop solar panel" style="background:linear-gradient(#3e5a95,#6d86b8 55%,#2c3f78)"></div></div>
  <div class="abs feature-title" style="left:133px"><b>Low</b> Cost</div>
  <div class="abs feature-frame" style="left:451px"><div class="feature-photo" role="img" aria-label="Vertical axis wind turbine against a blue sky" style="background:linear-gradient(160deg,#2a5fb8,#0f3a92 70%,#2c56a8)"></div></div>
  <div class="abs feature-title" style="left:451px"><b>Safe &amp;</b> Secured</div>
  <div class="abs feature-frame" style="left:766px"><div class="feature-photo" role="img" aria-label="Row of blue water treatment tanks with pipework" style="background:linear-gradient(#cfc7b4,#4f93c8 40%,#2f78b4 70%,#8a8a82)"></div></div>
  <div class="abs feature-title" style="left:766px"><b>Long</b> lasting</div>
</section>

<section class="abs about">
  <h2 class="abs about-title"><b>About</b> us</h2>
  <div class="abs about-rule"></div>
  <p class="abs about-copy">Lorem ipsum dolor sit amet, consectetur adipiscing elit. Nam lobortis dolor cursus nisl suscipit convallis. Fusce cursus velit at nisl fringilla commodo. Aenean semper odio orci, vel consequat metus euismod at. Phasellus porttitor ipsum sapien, vitae lacinia sem ultricies ut. Fusce tincidunt nisi non sem mattis, at rhoncus mauris dictum.</p>
  <a class="abs social footer-icon" style="left:481px;background:var(--tw)" aria-label="Social network link"></a>
  <a class="abs social footer-icon" style="left:528px;background:var(--li)" aria-label="Social network link"></a>
  <a class="abs social footer-icon" style="left:575px;background:var(--fb)" aria-label="Social network link"></a>
  <a class="abs social footer-icon" style="left:624px;background:var(--yt)" aria-label="Social network link"></a>
</section>

<footer class="abs footer">
  <div class="abs footer-links">FAQ<span>/</span>Sitemap<span>/</span>Product Information<span>/</span>Customer Service</div>
  <div class="abs copyright">Copyright © 2013 Lanternvale Summit</div>
</footer>
</body>
</html>
```